Contractor Business Card Design

Looking to have a card made that has a bold description of (KITCHENS, BASEMENTS, BATHROOMS)

Definition and layers a plus

Contact info is;

Mark T. Ellery
Fairhollow, MN 55990
Cell: 612-555-0147
website: www.cobaltfinishworks.example
Email: cobaltfinishworksmn@mailbox.example

colors: red, black, gray, white

Contact Information for Business Card

Contact info is;

Mark T. Ellery
Fairhollow, MN 55990
Cell: 612-555-0147

Colors
ec1f27

Requirements
Must have
• Looking for layers and definition
Nice to have
• Cards are planned to be printed on plastic cards

```html
<!DOCTYPE html>
<html lang="en">
<head>
<meta charset="utf-8">
<title>Cobalt Finish Works – Business Card Design</title>
<link rel="stylesheet" href="https://fonts.googleapis.com/css2?family=Arimo:wght@400&family=Poppins:wght@400;600;700&display=swap">
<style>
  :root {
    --red: #ec1f27;
    --black: #111111;
    --gray: #999999;
    --faint: #e4e4e4;
    --white: #ffffff;
  }
  * { box-sizing: border-box; margin: 0; padding: 0; }
  html, body { width: 1200px; height: 927px; overflow: hidden; background: var(--white); }
  .sheet { position: relative; width: 1200px; height: 927px; font-family: "Poppins", sans-serif; color: var(--black); }

  .sheet-title { position: absolute; top: 70px; left: 0; width: 1200px; text-align: center; font-family: "Arimo", sans-serif; color: #000; }
  .sheet-title h1 { font-weight: 400; font-size: 37px; line-height: 42px; }
  .sheet-title p { font-size: 27px; line-height: 32px; }
  .sheet-title .option { margin-top: 32px; }

  .card { position: absolute; top: 374px; width: 483px; height: 276px; border: 1px solid var(--gray); background: var(--white); overflow: hidden; }
  .card--front { left: 67px; }
  .card--back { left: 638px; }

  .backdrop-ring { position: absolute; left: 0; top: 0; }

  .brand { position: absolute; display: flex; flex-direction: column; align-items: center; text-align: center; }
  .brand-circle { border: 3px solid var(--red); border-radius: 50%; }
  .brand-name { font-weight: 700; color: var(--black); text-transform: uppercase; line-height: 1.1; }

  .card--front .brand { left: 20px; top: 34px; width: 150px; }
  .card--front .brand-circle { width: 66px; height: 66px; margin-bottom: 10px; }
  .card--front .brand-name { font-size: 17px; }

  .card--back .brand { left: 121px; top: 62px; width: 240px; }
  .card--back .brand-circle { width: 86px; height: 86px; margin-bottom: 14px; }
  .card--back .brand-name { font-size: 24px; }

  .holder-name { position: absolute; left: 214px; top: 32px; font-weight: 700; font-size: 18px; }

  .contact-list { position: absolute; left: 216px; top: 90px; list-style: none; }
  .contact-list li { display: flex; align-items: center; height: 31px; font-size: 12.5px; white-space: nowrap; }
  .contact-list li.email { font-size: 11.5px; }
  .contact-list svg { width: 12px; height: 12px; margin-right: 8px; flex: none; }

  .services { position: absolute; left: 21px; top: 233px; display: flex; gap: 14px; }
  .service { width: 138px; height: 23px; background: var(--red); color: var(--white); font-family: "Arimo", sans-serif; font-size: 16px; line-height: 23px; text-align: center; }

  .back-frame { position: absolute; left: 22px; top: 18px; width: 439px; height: 239px; border: 4px solid var(--red); }
</style>
</head>
<body>
<main class="sheet">
  <header class="sheet-title">
    <h1>Cobalt Finish Works</h1>
    <p>Business Card Design</p>
    <p class="option">Option -1</p>
  </header>

  <section class="card card--front">
    <svg class="backdrop-ring" width="483" height="276" aria-hidden="true">
      <circle cx="413" cy="121" r="97" fill="none" stroke="var(--faint)" stroke-width="10"/>
    </svg>

    <div class="brand">
      <div class="brand-circle"></div>
      <div class="brand-name">Cobalt<br>Finish Works</div>
    </div>

    <h2 class="holder-name">Mark T. Ellery</h2>

    <ul class="contact-list">
      <li>
        <svg viewBox="0 0 12 12"><path d="M6 0.5a4 4 0 0 0-4 4c0 3 4 7 4 7s4-4 4-7a4 4 0 0 0-4-4zm0 5.6a1.6 1.6 0 1 1 0-3.2 1.6 1.6 0 0 1 0 3.2z" fill="var(--red)"/></svg>
        Fairhollow, MN 55990
      </li>
      <li>
        <svg viewBox="0 0 12 12"><rect x="3" y="0.8" width="6" height="10.4" rx="1" fill="none" stroke="var(--red)" stroke-width="1.3"/><line x1="5" y1="9.4" x2="7" y2="9.4" stroke="var(--red)" stroke-width="1"/></svg>
        612-555-0147
      </li>
      <li class="email">
        <svg viewBox="0 0 12 12"><rect x="0.5" y="2.5" width="11" height="7.5" fill="var(--red)"/><path d="M0.5 2.8 6 6.8l5.5-4" fill="none" stroke="var(--white)" stroke-width="0.9"/></svg>
        cobaltfinishworksmn@mailbox.example
      </li>
      <li>
        <svg viewBox="0 0 12 12" fill="none" stroke="var(--red)" stroke-width="1"><circle cx="6" cy="6" r="5"/><ellipse cx="6" cy="6" rx="2.2" ry="5"/><line x1="1" y1="6" x2="11" y2="6"/><line x1="1.8" y1="3.5" x2="10.2" y2="3.5"/><line x1="1.8" y1="8.5" x2="10.2" y2="8.5"/></svg>
        www.cobaltfinishworks.example
      </li>
    </ul>

    <div class="services">
      <div class="service">KITCHENS</div>
      <div class="service">BASEMENTS</div>
      <div class="service">BATHROOMS</div>
    </div>
  </section>

  <section class="card card--back">
    <div class="back-frame"></div>
    <div class="brand">
      <div class="brand-circle"></div>
      <div class="brand-name">Cobalt<br>Finish Works</div>
    </div>
  </section>
</main>
</body>
</html>
```